Design my dad a new business card because his current one sucks!

I need a business card designed for my fathers home maintenance business. His customers are individuals (single moms, old people etc.) as well as the occasional business. As such it needs to be accessible to both target audiences.

The front of the card should be dark grey on yellow with the logo and contain the following information:
- Darren Whitlock
- 0488 372 915
- info@bluegumhomecare.example.au
- 0488 372 915

- ABN: 71 284 630 912
- 'Fully Insured'

The reverse should be yellow on dark grey and will have the web address:
- bluegumhomecare.example.au

And a few key services he offers:
GENERAL REPAIRS
PAINTING/TILING/
PAVING &CONCRETING
PRESSURE WASHING
ON-SITE WELDING
DECKING ADDITIONS & REPAIRS
FENCING
FULL BOND CLEANING

This will be first time the logo has been printed so you will need to come up with the best CMYK approximation of the RGB colours to make sure it is a close as possible.

```html
<!DOCTYPE html>
<html lang="en">
<head>
<meta charset="utf-8">
<title>Bluegum Home Care – Business Card</title>
<link rel="stylesheet" href="https://fonts.googleapis.com/css2?family=Open+Sans:wght@400;600;700&family=Roboto+Condensed:wght@400;700&display=swap">
<style>
  :root {
    --yellow: #f7d501;
    --yellow-deep: #f2b705;
    --charcoal: #3a3a3c;
    --charcoal-dark: #2a2a2b;
    --backdrop: #e9e6e0;
  }
  * { box-sizing: border-box; margin: 0; padding: 0; }
  html, body { width: 1200px; height: 913px; overflow: hidden; }
  body {
    background: var(--backdrop);
    font-family: "Open Sans", Arial, sans-serif;
    position: relative;
  }
  .card {
    position: absolute;
    top: 291px;
    width: 540px;
    height: 330px;
    border-radius: 4px;
    overflow: hidden;
    box-shadow: 0 8px 24px rgba(0,0,0,.22);
  }
  .card--front { left: 40px; background: var(--yellow); }
  .card--back { left: 620px; background: var(--charcoal); }
  .card__art { position: absolute; inset: 0; width: 100%; height: 100%; }

  .brand {
    position: absolute;
    display: flex;
    align-items: center;
    gap: 8px;
    font-weight: 700;
    font-size: 26px;
    letter-spacing: -.3px;
    white-space: nowrap;
  }
  .brand__dot { width: 22px; height: 22px; border-radius: 50%; }
  .card--front .brand { top: 18px; right: 60px; color: var(--charcoal); }
  .card--front .brand__dot { background: var(--charcoal); }
  .card--back .brand { top: 58px; left: 50%; transform: translateX(-50%); color: var(--yellow); font-size: 30px; }
  .card--back .brand__dot { background: var(--yellow); }

  .owner { position: absolute; left: 36px; top: 122px; color: var(--charcoal); }
  .owner__name { font-size: 20px; font-weight: 400; }
  .owner__role { font-size: 12px; font-weight: 700; margin-top: -2px; }

  .contact {
    position: absolute; left: 40px; top: 192px;
    font-family: "Roboto Condensed", Arial, sans-serif;
    font-size: 13.5px; line-height: 19px; color: var(--charcoal);
  }
  .contact dt { display: inline; font-weight: 700; }
  .contact dd { display: inline; margin-left: 2px; }
  .contact dd::after { content: ""; display: block; }

  .insured {
    position: absolute; right: 36px; top: 182px;
    color: var(--yellow); font-size: 19px; font-weight: 400;
    white-space: nowrap;
  }

  .services {
    position: absolute; left: 0; right: 0; top: 140px;
    list-style: none; text-align: center;
    font-family: "Roboto Condensed", Arial, sans-serif;
    font-size: 14px; line-height: 24px; letter-spacing: .2px;
    color: var(--yellow); padding: 0 12px;
  }
  .services li { display: inline; white-space: nowrap; }
  .services li + li::before { content: "\2022"; margin: 0 7px; }
  .services .break { display: block; height: 0; }

  .web-band {
    position: absolute; left: 0; right: 0; top: 234px; height: 44px;
    background: linear-gradient(90deg, var(--yellow-deep), var(--yellow) 40%);
    display: flex; align-items: center; justify-content: flex-end; padding-right: 36px;
    color: var(--charcoal-dark); font-size: 19px; font-weight: 600;
    white-space: nowrap;
  }
</style>
</head>
<body>

  <section class="card card--front" aria-label="Card front">
    <svg class="card__art" viewBox="0 0 540 330" preserveAspectRatio="none" aria-hidden="true">
      <path d="M540 60 C 440 70, 380 150, 320 220 C 260 290, 150 312, 0 314 L0 330 L540 330 Z" fill="var(--charcoal)"/>
      <path d="M560 80 C 455 90, 400 170, 342 238 C 282 304, 160 322, -10 323" fill="none" stroke="var(--yellow)" stroke-width="6"/>
      <path d="M540 50 C 432 60, 372 140, 310 210 C 255 272, 140 300, 0 303" fill="none" stroke="var(--charcoal)" stroke-width="3"/>
    </svg>

    <div class="brand"><span class="brand__dot"></span>Bluegum Home Care</div>

    <div class="owner">
      <p class="owner__name">Darren Whitlock</p>
      <p class="owner__role">owner</p>
    </div>

    <dl class="contact">
      <dt>Ph:</dt><dd>0488 372 915</dd>
      <dt>Email:</dt><dd>info@bluegumhomecare.example.au</dd>
      <dt>ABN:</dt><dd>71 284 630 912</dd>
    </dl>

    <p class="insured">Fully Insured</p>
  </section>

  <section class="card card--back" aria-label="Card back">
    <div class="brand"><span class="brand__dot"></span>Bluegum Home Care</div>

    <ul class="services">
      <li>GENERAL REPAIRS</li><li>PAINTING/TILING</li><li>PAVING &amp; CONCRETING</li>
      <span class="break"></span>
      <li>PRESSURE WASHING</li><li>ON-SITE WELDING</li><li>DECKING ADDITIONS &amp; REPAIRS</li>
      <span class="break"></span>
      <li>FENCING</li><li>FULL BOND CLEANING</li>
    </ul>

    <div class="web-band">www.bluegumhomecare.example.au</div>
  </section>

</body>
</html>
```